Business Cards for a small business advisory (business services)

Professional look. Same as would apply for a lawyer, accountant, or other financial services professional. Please use the logo colors

Target Market(s)

small business owners

Industry/Entity Type

Financial Servics

Contact Information for Business Card

Name: Gavin L. Whitmore, CAIA / Title: Business Advisor / Office #: (718) 294-7716 / Mobile #: (917) 382-5047 / Email: g.whitmore@clearfieldventurepartners.example / Web: www.clearfieldventurepartners.example

Font styles to use
Sans Serif

```html
<!DOCTYPE html>
<html lang="en">
<head>
<meta charset="utf-8">
<title>Clearfield Venture Partners – Business Cards</title>
<link href="https://fonts.googleapis.com/css2?family=Montserrat:wght@400;500;600;700&display=swap" rel="stylesheet">
<style>
  :root {
    --navy: #1b3a6b;
    --green: #8cc63f;
    --white: #ffffff;
    --ink: #4a4a4a;
    --rule: #6f7f99;
    --stage: #3a3b3e;
  }
  * { box-sizing: border-box; margin: 0; padding: 0; }
  html, body { width: 1200px; height: 900px; overflow: hidden; }
  body {
    background: var(--stage);
    font-family: "Montserrat", sans-serif;
    position: relative;
  }
  .card {
    position: absolute;
    width: 600px;
    height: 343px;
    border-radius: 18px;
    overflow: hidden;
    box-shadow: 0 10px 30px rgba(0,0,0,.35);
  }
  .card-back { left: 80px; top: 70px; background: var(--navy); }
  .card-front { left: 520px; top: 487px; background: var(--white); }

  .brand { position: absolute; display: flex; align-items: center; white-space: nowrap; }
  .brand-dot { border-radius: 50%; flex: none; background: var(--green); }
  .brand-text { display: flex; flex-direction: column; }
  .brand-name { font-weight: 700; line-height: 1; letter-spacing: -0.5px; }
  .brand-tagline { font-weight: 600; text-transform: uppercase; letter-spacing: .3px; }

  .card-back .brand { left: 118px; top: 128px; gap: 16px; }
  .card-back .brand-dot { width: 34px; height: 34px; }
  .card-back .brand-name { color: var(--white); font-size: 64px; }
  .card-back .brand-tagline { color: var(--white); font-size: 7px; margin-top: 8px; }

  .card-front .brand { left: 46px; top: 146px; gap: 10px; }
  .card-front .brand-dot { width: 22px; height: 22px; }
  .card-front .brand-name { color: var(--navy); font-size: 38px; }
  .card-front .brand-tagline { color: var(--navy); font-size: 4.6px; margin-top: 5px; }

  .divider {
    position: absolute; left: 300px; top: 92px;
    width: 1px; height: 126px; background: var(--rule);
  }
  .person { position: absolute; left: 318px; top: 92px; white-space: nowrap; }
  .person-name { color: var(--navy); font-weight: 700; font-size: 17px; }
  .person-title { color: var(--green); font-weight: 500; font-size: 12px; margin-top: 2px; }
  .contacts { list-style: none; margin-top: 14px; }
  .contacts li {
    display: flex; align-items: center; gap: 7px;
    color: var(--ink); font-size: 10px; line-height: 17px;
  }
  .contacts svg { width: 10px; height: 10px; flex: none; fill: var(--green); }

  .band-navy { position: absolute; left: 0; bottom: 0; width: 66%; height: 14px; background: var(--navy); }
  .band-green { position: absolute; right: 0; bottom: 0; width: 34%; height: 26px; background: var(--green); }
</style>
</head>
<body>
  <section class="card card-back" aria-label="Card back">
    <div class="brand">
      <span class="brand-dot"></span>
      <div class="brand-text">
        <span class="brand-name">Clearfield</span>
        <span class="brand-tagline">Steady advice for owners ready to buy or sell their company</span>
      </div>
    </div>
  </section>

  <section class="card card-front" aria-label="Card front">
    <div class="brand">
      <span class="brand-dot"></span>
      <div class="brand-text">
        <span class="brand-name">Clearfield</span>
        <span class="brand-tagline">Steady advice for owners ready to buy or sell their company</span>
      </div>
    </div>

    <div class="divider"></div>

    <div class="person">
      <div class="person-name">Gavin L. Whitmore, CAIA</div>
      <div class="person-title">Business Advisor</div>
      <ul class="contacts">
        <li><svg viewBox="0 0 10 10"><path d="M1 3.5C1 2 2.5 1 5 1s4 1 4 2.5L7.5 4.2 6.8 3H3.2L2.5 4.2zM2.5 5h5l1 4h-7z"/></svg>(718) 294-7716</li>
        <li><svg viewBox="0 0 10 10"><path d="M3 0.5h4a.8.8 0 0 1 .8.8v7.4a.8.8 0 0 1-.8.8H3a.8.8 0 0 1-.8-.8V1.3A.8.8 0 0 1 3 .5zM3.2 1.6v6h3.6v-6z"/></svg>(917) 382-5047</li>
        <li><svg viewBox="0 0 10 10"><path d="M0.5 2h9v6h-9zM1 2.5l4 3 4-3"/></svg>g.whitmore@clearfieldventurepartners.example</li>
        <li><svg viewBox="0 0 10 10"><circle cx="5" cy="5" r="4.5"/></svg>www.clearfieldventurepartners.example</li>
      </ul>
    </div>

    <div class="band-navy"></div>
    <div class="band-green"></div>
  </section>
</body>
</html>
```